依頼概要
初めまして。本書は、会社等の会議を実施する立場の人に向けてのものと
なっております。
■依頼の目的/概要
lumora出版、ビジネスパーソン向け書籍の表紙デザインをお願いします。
今のところ、題名は
「だれでも週末から家庭菜園がはかどる」

■本の内容
会社等で、会議をうまく進めていきたいがなかなか思うように
薦められない方向けに、誰でも簡単にこれだけのことを実践すれば
会議が上手く進められるというポイントをまとめたものになっております。

■デザイン要望
ビジネスパーソン向けですが、会議等に不慣れな方向けで
あまり難しく考えなくても、誰でも簡単にトライできるという
イメージを持ってもらえるようにしたいです。

現在、原稿は9割がたできております。添付ファイルをご参照ください。

その他何かご不明な点がございましたら、お気軽にご質問下さい。
よろしくお願いいたします。
名前は、ペンネームにする予定です。
今のところ、柚木 瑛之助が候補です。
■ 選んだ理由

私のイメージする会社内での和気あいあいとした雰囲気のイラストがまずは
気に入りました。
ターゲットが、会議がうまくできない人向けなので、なるべくそれを意識して
親しみやすいものを選びました。

■ 提案者全員のお礼・コメント

今回は、ターゲットが初心者向けであったので、親しみやすいものを選びましたが、
例えば、会議を上から見たイラストなどは、斬新なアイデアで印象深く
ターゲットが違えば、選んでいたと思います。
中身を理解して、提案いただけた方も多く、感謝いたします。
今後も、このシリーズを出版していきたいと考えておりますので
次の機会もよろしくお願いいたします。
ありがとうございました。

```html
<!DOCTYPE html>
<html lang="ja">
<head>
<meta charset="utf-8">
<title>だれでも週末から家庭菜園がはかどる</title>
<link rel="stylesheet" href="https://fonts.googleapis.com/css2?family=Noto+Sans+JP:wght@500;700;900&display=swap">
<style>
  :root {
    --paper: #ffffff;
    --ink: #1a1a1a;
    --accent: #e5282d;
    --scene-a: #e9eef5;
    --scene-b: #d6e1ee;
  }
  * { margin: 0; padding: 0; box-sizing: border-box; }
  html, body { width: 752px; height: 1200px; overflow: hidden; background: var(--paper); }
  .cover {
    position: relative;
    width: 752px;
    height: 1200px;
    background: var(--paper);
    font-family: "Noto Sans JP", sans-serif;
    color: var(--ink);
  }
  .vertical {
    position: absolute;
    writing-mode: vertical-rl;
    font-weight: 900;
    line-height: 1;
    z-index: 2;
  }
  .red { color: var(--accent); }
  .title-col-1 { top: 28px; left: 652px; font-size: 80px; }
  .title-col-2 { top: 28px; left: 564px; font-size: 80px; }
  .title-col-3 { top: 28px; left: 476px; font-size: 72px; }
  .title-col-3 .small { font-size: 54px; color: var(--ink); }
  .title-col-4 { top: 52px; left: 384px; font-size: 78px; }
  .author { top: 34px; left: 40px; font-size: 54px; letter-spacing: 0.04em; }
  .scene {
    position: absolute;
    left: 20px; top: 392px;
    width: 712px; height: 408px;
    background: linear-gradient(180deg, var(--scene-a), var(--scene-b));
    border-radius: 12px;
    z-index: 1;
  }
  .badge {
    position: absolute;
    left: 165px; top: 352px;
    width: 150px; height: 150px;
    border-radius: 50%;
    background: var(--paper);
    border: 3px solid var(--ink);
    display: flex; flex-direction: column; align-items: center; justify-content: center;
    font-weight: 900; font-size: 22px; line-height: 1.4; text-align: center;
    z-index: 3;
  }
  .badge .num { font-size: 28px; }
  .lead {
    position: absolute;
    left: 0; right: 0; top: 818px;
    text-align: center;
    font-weight: 700;
    font-size: 30px;
    line-height: 1.9;
  }
  .tagline {
    position: absolute;
    left: 0; right: 0; top: 975px;
    text-align: center;
    font-weight: 900;
    font-size: 108px;
    line-height: 1.1;
  }
</style>
</head>
<body>
<main class="cover">
  <div class="vertical title-col-1">だれでも</div>
  <div class="vertical title-col-2"><span class="red">週末</span>から</div>
  <div class="vertical title-col-3"><span class="red">家庭菜園</span><span class="small">が</span></div>
  <div class="vertical title-col-4"><span class="red">はかどる</span></div>

  <div class="vertical author">柚木 瑛之助</div>

  <div class="scene" role="img" aria-label="明るいオフィスで和やかに会議をする人々のイラスト"></div>

  <div class="badge"><span>この<span class="num">1</span>冊で</span><span>問題解決!!</span></div>

  <p class="lead">会議をうまく進めたい方へ。<br>準備は『アジェンダ』と『終了条件』の2つだけ。</p>

  <p class="tagline">会議の<span class="red">必読書</span></p>
</main>
</body>
</html>
```